A Weather Forecasting Site needs designs

We need a website design for our new venture which is a weather forecasting website. This website should have the latest design trends.

Menu
Weather, Maps, Videos and Photos

The home page requirements are as follows:
- Search Bar
- Local Weather
- Weather forecast of major cities in the World
Favorite locations
- Space for ADs
- Email signup

Weather Details page
This page will be redirected from the home page when you click on any of the weather forecast section

We are open to all kinds of designs and ideas. Feel free to you colors which suite your design.

```html
<!DOCTYPE html>
<html lang="en">
<head>
<meta charset="utf-8">
<title>SkyCaster — Weather Forecast</title>
<link rel="stylesheet" href="https://fonts.googleapis.com/css2?family=Montserrat:wght@300;400;500;600;700;800&family=Lobster&display=swap">
<style>
:root{
  --red:#e84c3d;
  --red-dark:#d7412f;
  --blue:#2a7fc9;
  --navy:#2a2d33;
  --navy-deep:#212328;
  --page:#fafafa;
  --panel:#f4f3f3;
  --line:#e3e3e3;
  --text:#333;
  --muted:#777;
  --white:#fff;
}
*{box-sizing:border-box;margin:0;padding:0}
html,body{width:1200px;height:2239px;overflow:hidden}
body{position:relative;background:var(--page);font-family:"Montserrat",sans-serif;color:var(--text)}
.abs{position:absolute}

/* top navigation */
.topband{left:0;top:0;width:1200px;height:78px;background:var(--navy-deep)}
.mainnav{left:146px;top:0;width:906px;height:96px;background:var(--navy);display:flex}
.mainnav::before{content:"";position:absolute;left:0;top:0;width:906px;height:6px;background:linear-gradient(90deg,var(--red) 0 152px,var(--blue) 152px)}
.mainnav a{color:var(--white);text-decoration:none;font-size:13px;font-weight:600;letter-spacing:.3px;display:flex;align-items:center;justify-content:center;border-right:1px solid #3a3d44;height:96px}
.mainnav a:last-child{border-right:none}

/* header */
.brand{left:146px;top:142px;display:flex;align-items:center;gap:12px}
.brand-dot{width:40px;height:40px;border-radius:50%;background:var(--red)}
.brand-name{font-size:40px;font-weight:400;color:var(--navy);letter-spacing:-.5px}
.account{left:743px;top:136px;height:46px;display:flex}
.account a{display:flex;align-items:center;gap:10px;color:var(--white);font-size:12px;font-weight:600;text-decoration:none;padding:0 22px}
.btn-open{background:var(--navy);width:206px}
.btn-login{background:var(--red);width:103px}

/* search */
.searchbox{left:146px;top:230px;width:906px;height:86px;background:#ebebeb;box-shadow:0 3px 6px rgba(0,0,0,.18);z-index:3}
.search-input{position:absolute;left:21px;top:25px;width:715px;height:36px;background:var(--white);font-size:10px;color:#aaa;padding-left:16px;line-height:36px;letter-spacing:.3px}
.search-btn{position:absolute;left:736px;top:25px;width:37px;height:36px;background:var(--blue);display:flex;align-items:center;justify-content:center}
.unit{position:absolute;top:25px;width:36px;height:36px;display:flex;align-items:center;justify-content:center;color:var(--white);font-size:16px}
.unit-c{left:796px;background:var(--navy)}
.unit-f{left:849px;background:var(--red)}

/* hero */
.hero{left:0;top:291px;width:1200px;height:445px;background:linear-gradient(180deg,#26506b 0%,#5d8fa6 35%,#a9c0c4 60%,#c8a476 85%,#8c6a3e 100%)}
.hero-title{left:0;top:420px;width:1180px;text-align:center;color:var(--red);font-family:"Lobster",cursive;line-height:1}
.hero-title small{display:block;font-size:20px;margin-left:-60px}
.hero-title strong{font-size:46px;font-weight:400}
.featured{left:146px;top:545px;width:906px;height:191px;background:rgba(70,88,98,.72)}
.featured .arrow{position:absolute;top:80px}
.feat-temps{position:absolute;left:428px;top:58px;color:var(--white);font-size:28px;font-weight:300;display:flex;gap:22px;align-items:center}
.feat-city{position:absolute;left:400px;top:98px;width:500px;color:var(--white)}
.feat-city h2{font-size:46px;font-weight:700;line-height:1}
.feat-city p{font-size:20px;font-weight:400;margin-left:42px}
.forecast{left:146px;top:736px;width:906px;height:124px;background:var(--red);display:flex}
.day{flex:1;border-right:1px solid #f06a5c;color:var(--white);text-align:center;padding-top:14px}
.day:last-child{border-right:none}
.day h4{font-size:16px;font-weight:500}
.day .temps{font-size:15px;font-weight:500;margin-top:4px}

/* local weather */
.section-title{font-size:30px;font-weight:600;color:var(--navy);letter-spacing:-.5px}
.local-title{left:146px;top:922px}
.updated{left:147px;top:961px;font-size:9px;color:var(--muted)}
.local{left:146px;top:997px;width:906px;height:219px;border:1px solid var(--line);background:var(--white)}
.local-photo{position:absolute;left:0;top:0;width:264px;height:193px;background:linear-gradient(180deg,#5a6d96,#3b4a6d 60%,#c99a55)}
.local-now{position:absolute;left:264px;top:0;width:180px;height:193px;background:#2a5478}
.local-temp{position:absolute;left:30px;top:120px;color:var(--white);font-size:36px;font-weight:400;display:flex;align-items:center;gap:4px}
.local-temp small{font-size:12px;line-height:1.1;text-align:center}
.caption{position:absolute;left:0;top:193px;width:444px;height:26px;background:#6e9bd1;color:var(--white);font-size:13px;font-weight:600;display:flex;justify-content:space-between;align-items:center;padding:0 12px}
.caption span:last-child{font-weight:500}
.details{position:absolute;left:444px;top:0;width:461px}
.details div{height:36px;display:flex;align-items:center;font-size:16px;font-weight:300;color:#444;padding-left:40px}
.details div:nth-child(odd){background:#f6f6f6}
.details span:first-child{width:254px}

/* favorites */
.favorites{left:146px;top:1276px;width:906px;height:408px;background:var(--panel)}
.fav-title{position:absolute;left:22px;top:28px;font-size:22px;font-weight:600;color:var(--navy)}
.fav-rule{position:absolute;left:22px;top:66px;width:862px;height:1px;background:#d8d8d8}
.fav-nav{position:absolute;top:30px;width:36px;height:36px;display:flex;align-items:center;justify-content:center}
.fav-prev{left:812px;background:var(--navy)}
.fav-next{left:848px;background:var(--red)}
.card{position:absolute;top:93px;width:258px}
.card-img{width:258px;height:146px}
.card h5{color:var(--red);font-size:14px;font-weight:600;margin-top:16px}
.card p{font-size:11px;line-height:17px;color:#555;margin-top:6px}
.card a{display:inline-block;margin-top:19px;width:116px;height:36px;line-height:36px;text-align:center;color:var(--white);font-size:10px;font-weight:700;background:var(--navy-deep);border-radius:3px;text-decoration:none}
.card a.active{background:var(--red)}

/* newsletter */
.newsletter{left:146px;top:1748px;width:906px;height:88px;background:var(--red);color:var(--white)}
.newsletter h3{position:absolute;left:100px;top:27px;font-size:26px;font-weight:300}
.newsletter h3 b{font-weight:700}
.email{position:absolute;left:488px;top:25px;width:314px;height:39px;border:1px solid rgba(255,255,255,.8);border-radius:4px;font-size:12px;padding-left:12px;line-height:37px}

/* ad */
.ad{left:146px;top:1872px;width:906px;height:135px;background:linear-gradient(180deg,#8c9aa3 0%,#7d8b72 45%,#4e6b2c 100%);color:var(--white)}
.ad-text{position:absolute;left:368px;top:36px;line-height:1}
.ad-text strong{font-size:42px;font-weight:800;display:block;letter-spacing:-1px}
.ad-text span{font-size:14px;font-weight:500;margin-left:2px}

/* footer */
.footer{left:0;top:2057px;width:1200px;height:137px;background:var(--navy)}
.footnav{position:absolute;left:146px;top:34px;width:906px;display:flex}
.footnav a{flex:1;text-align:center;font-size:11px;color:#b9bbbf;text-decoration:none;border-right:1px solid #444850}
.footnav a:last-child{border-right:none}
.social{position:absolute;left:542px;top:83px;display:flex;gap:3px}
.social i{width:33px;height:33px;background:var(--red);display:block}
.copy{left:0;top:2194px;width:1200px;height:45px;background:var(--navy-deep);color:#8b8e94;font-size:10px;text-align:center;line-height:45px}
</style>
</head>
<body>

<svg width="0" height="0" style="position:absolute" aria-hidden="true">
  <defs>
    <symbol id="cloud" viewBox="0 0 40 26"><path d="M10 26a9 9 0 0 1-1-18 11 11 0 0 1 21 2 8 8 0 0 1 1 16z" fill="currentColor"/></symbol>
    <symbol id="rain" viewBox="0 0 40 40"><path d="M10 24a8 8 0 0 1-1-16 10 10 0 0 1 19 2 7 7 0 0 1 1 14z" fill="currentColor"/><path d="M12 29l-2 5M19 29l-2 5M26 29l-2 5" stroke="currentColor" stroke-width="2" stroke-linecap="round"/></symbol>
  </defs>
</svg>

<div class="abs topband"></div>
<nav class="abs mainnav">
  <a style="width:154px">HOME</a><a style="width:151px">WEATHER</a><a style="width:150px">MAPS</a><a style="width:141px">VIDEOS</a><a style="width:136px">PHOTOS</a><a style="width:174px">CONTACTS</a>
</nav>

<header>
  <div class="abs brand"><span class="brand-dot"></span><span class="brand-name">SKYCASTER</span></div>
  <div class="abs account">
    <a class="btn-open" href="#"><svg width="10" height="11" viewBox="0 0 10 11"><circle cx="5" cy="3" r="3" fill="#fff"/><path d="M0 11a5 5 0 0 1 10 0z" fill="#fff"/></svg>OPEN AN ACCOUNT</a>
    <a class="btn-login" href="#"><svg width="9" height="11" viewBox="0 0 9 11"><rect y="5" width="9" height="6" fill="#fff"/><path d="M2 5V3a2.5 2.5 0 0 1 5 0v2" stroke="#fff" fill="none" stroke-width="1.5"/></svg>LOGIN</a>
  </div>
</header>

<div class="abs searchbox">
  <div class="search-input">SEARCH ZIP, CITY, OR PLACE...</div>
  <div class="search-btn"><svg width="16" height="16" viewBox="0 0 16 16"><circle cx="6.5" cy="6.5" r="4.8" stroke="#fff" stroke-width="2.2" fill="none"/><path d="M10 10l4.5 4.5" stroke="#fff" stroke-width="2.5" stroke-linecap="round"/></svg></div>
  <div class="unit unit-c">C°</div>
  <div class="unit unit-f">F°</div>
</div>

<section>
  <div class="abs hero" role="img" aria-label="Photo of a cloudy sky with a hot air balloon over the horizon"></div>
  <div class="abs hero-title"><small>Weather</small><strong>Major Cities</strong></div>
  <div class="abs featured">
    <svg class="arrow" style="left:22px" width="18" height="14" viewBox="0 0 18 14"><path d="M8 1L2 7l6 6M2 7h15" stroke="#e84c3d" stroke-width="2.5" fill="none"/></svg>
    <svg class="arrow" style="left:864px" width="18" height="14" viewBox="0 0 18 14"><path d="M10 1l6 6-6 6M16 7H1" stroke="#e84c3d" stroke-width="2.5" fill="none"/></svg>
    <svg style="position:absolute;left:208px;top:30px" width="120" height="130" viewBox="0 0 120 130">
      <g stroke="#fff" stroke-width="7" stroke-linecap="round"><path d="M62 8v14M90 18l-9 10M104 44H90M34 18l9 10M20 44h14"/></g>
      <path d="M38 58a26 26 0 0 1 50-4" stroke="#fff" stroke-width="7" fill="none"/>
      <path d="M24 128a20 20 0 0 1-2-40 26 26 0 0 1 49-6 22 22 0 0 1 14 46z" fill="#fff"/>
    </svg>
    <div class="feat-temps">
      <span><svg width="12" height="28" viewBox="0 0 12 28"><rect x="3" y="1" width="6" height="18" rx="3" stroke="#fff" fill="none" stroke-width="1.5"/><circle cx="6" cy="22" r="5" fill="#fff"/></svg> 35°</span>
      <span><svg width="26" height="24" viewBox="0 0 26 24"><path d="M1 12a12 12 0 0 1 24 0z" fill="#fff"/><path d="M13 12v9a2 2 0 0 1-4 0" stroke="#fff" stroke-width="2" fill="none"/></svg> 29°</span>
    </div>
    <div class="feat-city"><h2>Auckland</h2><p>New Zealand</p></div>
  </div>
  <div class="abs forecast">
    <div class="day"><h4>MON</h4><svg width="44" height="40" style="color:#fff"><use href="#rain"/></svg><div class="temps">31° 25°</div></div>
    <div class="day"><h4>TUE</h4><svg width="44" height="40" style="color:#fff"><use href="#rain"/></svg><div class="temps">31° 26°</div></div>
    <div class="day"><h4>WED</h4><svg width="44" height="40" style="color:#fff"><use href="#rain"/></svg><div class="temps">30° 25°</div></div>
    <div class="day"><h4>THU</h4><svg width="44" height="40" style="color:#fff"><use href="#rain"/></svg><div class="temps">31° 27°</div></div>
    <div class="day"><h4>FRI</h4><svg width="44" height="40" style="color:#fff"><use href="#rain"/></svg><div class="temps">29° 25°</div></div>
    <div class="day"><h4>SAT</h4><svg width="44" height="40" style="color:#fff"><use href="#rain"/></svg><div class="temps">31° 26°</div></div>
  </div>
</section>

<section>
  <h2 class="abs section-title local-title">Local Weather</h2>
  <p class="abs updated">UPDATED 12.50 PM ET</p>
  <div class="abs local">
    <div class="local-photo" role="img" aria-label="Evening city skyline of Paris with the Eiffel Tower"></div>
    <div class="local-now">
      <svg style="position:absolute;left:32px;top:25px" width="100" height="86" viewBox="0 0 100 86"><path d="M60 10a20 20 0 1 0 30 26 22 22 0 0 1-30-26z" stroke="#fff" stroke-width="5" fill="none" opacity=".85"/><path d="M22 80a16 16 0 0 1-2-32 22 22 0 0 1 42-4 18 18 0 0 1 6 36z" stroke="#fff" stroke-width="5" fill="#2a5478"/></svg>
      <div class="local-temp"><small>24<br>9</small>22<span style="font-size:18px;align-self:flex-start">o</span> C</div>
    </div>
    <div class="caption"><span>Paris, France</span><span>Monday, September 30, 2017</span></div>
    <div class="details">
      <div><span>Feels like:</span><span>26°</span></div>
      <div><span>Humidity:</span><span>71%</span></div>
      <div><span>Wind:</span><span>S 10 mph</span></div>
      <div><span>Sunrise:</span><span>6:31 AM</span></div>
      <div><span>Sunset:</span><span>8:52 PM</span></div>
      <div><span>Barometer:</span><span>30.03" Hg</span></div>
    </div>
  </div>
</section>

<section class="abs favorites">
  <h3 class="fav-title">Favorite Locations</h3>
  <div class="fav-rule"></div>
  <div class="fav-nav fav-prev"><svg width="8" height="12" viewBox="0 0 8 12"><path d="M7 1L2 6l5 5" stroke="#fff" stroke-width="2" fill="none"/></svg></div>
  <div class="fav-nav fav-next"><svg width="8" height="12" viewBox="0 0 8 12"><path d="M1 1l5 5-5 5" stroke="#fff" stroke-width="2" fill="none"/></svg></div>
  <div class="card" style="left:24px">
    <div class="card-img" role="img" aria-label="City skyline with a tall skyscraper" style="background:linear-gradient(180deg,#9fb3cc,#6d7a88 60%,#4c4f52)"></div>
    <h5>CITY NAME</h5><p>Lorem ipsum dolor sit amet, consectetur adipisicing elit, sed do eiusmod tempor.</p><a href="#">VIEW WEATHER</a>
  </div>
  <div class="card" style="left:323px">
    <div class="card-img" role="img" aria-label="Historic hilltop castle hotel above a harbour at dusk" style="background:linear-gradient(180deg,#6a78a8,#7c6a7a 50%,#a25a3c)"></div>
    <h5>CITY NAME</h5><p>Lorem ipsum dolor sit amet, consectetur adipisicing elit, sed do eiusmod tempor.</p><a class="active" href="#">VIEW WEATHER</a>
  </div>
  <div class="card" style="left:626px">
    <div class="card-img" role="img" aria-label="Glass dome conservatory with gardens by the sea" style="background:linear-gradient(135deg,#1f5fa8,#5a9fd4 45%,#7aa564 75%,#d9e4ea)"></div>
    <h5>CITY NAME</h5><p>Lorem ipsum dolor sit amet, consectetur adipisicing elit, sed do eiusmod tempor.</p><a href="#">VIEW WEATHER</a>
  </div>
</section>

<section class="abs newsletter">
  <h3>Subscribe to our <b>Newsletter</b></h3>
  <div class="email">Your Email...</div>
  <svg style="position:absolute;left:758px;top:38px" width="30" height="12" viewBox="0 0 30 12"><path d="M0 6h24M19 1l6 5-6 5" stroke="#fff" stroke-width="3" fill="none"/></svg>
</section>

<aside class="abs ad" role="img" aria-label="Advertising space over a green countryside landscape">
  <svg style="position:absolute;left:300px;top:38px" width="62" height="60" viewBox="0 0 62 60"><path d="M20 40c6-22 20-34 40-38-4 20-16 34-38 40z" fill="#fff"/><path d="M14 30l10-4-6 12zM26 46l4-10-12 6z" fill="#fff"/><path d="M4 56l10-10M10 58l6-6" stroke="#fff" stroke-width="3" stroke-linecap="round"/></svg>
  <div class="ad-text"><strong>YOUR AD</strong><span>Goes here...</span></div>
</aside>

<footer>
  <div class="abs footer">
    <nav class="footnav"><a>HOME</a><a>WEATHER</a><a>MAPS</a><a>VIDEOS</a><a>PHOTOS</a><a>CONTACTS</a></nav>
    <div class="social"><i></i><i></i><i></i></div>
  </div>
  <div class="abs copy">©COPYRIGHT 2017. ALL RIGHTS ARE RESERVED.</div>
</footer>

</body>
</html>
```